Kelvo Tech Oz Business card revamp

We are looking to revamp our business card design. We are hoping to change our colours to dark navey blue, gray, white and black but are open to keeping the same if a good design is submited. We are after somthing a bit differnt not just boring business card. I have attached a copy of our current card. We Want to keep the same logo design which i have attached a few to hopfully help you in this process. We are after a design that can be personalized to separate 4 people

Colors
0455a3
ffffff
000000
cbcbcb

Requirements
Must have
• Kelvo Tech Logo, address 3/41 Mallory Court, Wexhill 4218, phone number, Name and position

```html
<!DOCTYPE html>
<html lang="en">
<head>
<meta charset="utf-8">
<title>Kelvo Tech business card</title>
<link rel="stylesheet" href="https://fonts.googleapis.com/css2?family=Roboto:wght@400;500;700&display=swap">
<style>
  :root {
    --navy: #05063c;
    --orange: #e8681f;
    --paper: #f4f4f4;
    --white: #ffffff;
    --stage: #d9d9d9;
  }
  * { box-sizing: border-box; margin: 0; padding: 0; }
  html, body { width: 1200px; height: 960px; overflow: hidden; }
  body {
    background: var(--stage);
    font-family: "Roboto", Arial, sans-serif;
    position: relative;
  }
  .card {
    position: absolute;
    width: 600px;
    height: 344px;
    box-shadow: 0 3px 6px rgba(0,0,0,0.35);
    overflow: hidden;
  }
  .card-front { left: 314px; top: 113px; background: var(--paper); }
  .card-back { left: 311px; top: 472px; background: var(--navy); }

  .brand {
    display: flex;
    align-items: center;
    gap: 10px;
    font-weight: 700;
    white-space: nowrap;
  }
  .brand-dot { border-radius: 50%; background: var(--orange); flex: none; }
  .front-brand { position: absolute; left: 38px; top: 74px; color: var(--navy); font-size: 30px; }
  .front-brand .brand-dot { width: 22px; height: 22px; }

  .person { position: absolute; right: 46px; top: 80px; text-align: right; }
  .person-name { color: var(--navy); font-weight: 500; font-size: 21px; letter-spacing: 0.3px; }
  .person-role { color: var(--orange); font-size: 14px; margin-top: 2px; }

  .contact-band {
    position: absolute; left: 0; top: 182px; width: 600px; height: 137px;
    background: var(--navy);
  }
  .address { position: absolute; left: 36px; top: 18px; color: var(--white); font-size: 14px; line-height: 19px; }
  .contact-list { position: absolute; left: 36px; top: 64px; list-style: none; color: var(--white); font-size: 14px; }
  .contact-list li { display: flex; align-items: center; gap: 9px; height: 19px; }
  .contact-list svg { width: 13px; height: 13px; flex: none; }
  .band-accent {
    position: absolute; right: 0; top: 0; width: 205px; height: 137px;
    background: linear-gradient(90deg, var(--navy) 0%, var(--orange) 30%, #e66a22 100%);
  }

  .back-brand { position: absolute; left: 0; right: 0; top: 138px; justify-content: center; color: var(--white); font-size: 40px; }
  .back-brand .brand-dot { width: 28px; height: 28px; }
  .services { position: absolute; left: 0; right: 0; top: 268px; text-align: center; color: var(--white); font-size: 14.5px; line-height: 18px; }
  .sep { color: var(--orange); margin: 0 3px; }
</style>
</head>
<body>
  <section class="card card-front" aria-label="Card front">
    <div class="brand front-brand"><span class="brand-dot"></span>Kelvo Tech</div>
    <div class="person">
      <div class="person-name">DANIEL MARSH</div>
      <div class="person-role">Director</div>
    </div>
    <div class="contact-band">
      <p class="address">3/41 Mallory Court,<br>Wexhill 4218</p>
      <ul class="contact-list">
        <li><svg viewBox="0 0 16 16"><path fill="#e8681f" d="M3 1l3 3-1.5 2c1 2 3 4 5 5l2-1.5 3 3-2 2C7 14 2 9 1 3z"/></svg>612 480 3917</li>
        <li><svg viewBox="0 0 16 16"><rect x="1" y="3" width="14" height="10" fill="#e8681f"/><path d="M1 3l7 6 7-6" fill="none" stroke="#05063c" stroke-width="1.4"/></svg>name@kelvotech.com.au</li>
        <li><svg viewBox="0 0 16 16"><circle cx="8" cy="8" r="7" fill="#e8681f"/><path d="M5 4c2 1 1 3 3 3s1 3 3 4" fill="none" stroke="#05063c" stroke-width="1.4"/></svg>www.kelvotech.com.au</li>
      </ul>
      <div class="band-accent" role="img" aria-label="Decorative brand symbol area"></div>
    </div>
  </section>

  <section class="card card-back" aria-label="Card back">
    <div class="brand back-brand"><span class="brand-dot"></span>Kelvo Tech</div>
    <p class="services">
      Service Fenotrations <span class="sep">•</span> Steel Spray coatings <span class="sep">•</span> Intumescent paint<br>
      Boot Spray &amp; Wrags <span class="sep">•</span> Fire&amp;Savoke Barriers <span class="sep">•</span> Fire Rated Walls Ceilings
    </p>
  </section>
</body>
</html>
```